BrightHarbor Flowchart Marketing Flyer

We are an MSP IT company. We have created a flowchart that we would like jazzed up to use in marketing new customers. The flowchart is a visual for prospective clients to see, in a simple way, what our process is. The flowchart should be 8.5"x11". We do not want the template of the flowchart altered (no boxes moved around) but would like something visually appealing and clean looking. Our office colors are lime green, royal blue, with accent colors of orange and purple. We would like the colors incorporated into the design. The design should be modern. This flyer is not going to be mass mailed. It will be handed to a prospective client in a face to face meeting.
Updates

I have uploaded our company logo to my brief in a couple of formats. One of the designers requested this. Great idea! I apologize for not providing it to begin with - it's my first time using this Website and the first time I have been assigned a project.

I was not able to view over the weekend as I did not have access to my work computer. Also need to review with the rest of management team on Thursday 6/28

Target Market(s)

Potential clients for an MSP IT company

Industry/Entity Type

It Company

Requirements
Must have
• The template itself we don't want changed. In other words we don't want the boxes moved around.
Nice to have
• Text, lines, shading and color of boxes can be changed. Not all colors mentioned in the brief need to be used. Would like it easy on the eye.

```html
<!DOCTYPE html>
<html lang="en">
<head>
<meta charset="utf-8">
<title>The BrightHarbor Process</title>
<link rel="stylesheet" href="https://fonts.googleapis.com/css2?family=Arimo:ital,wght@0,400;0,700;1,700&display=swap">
<style>
  :root {
    --orange: #e8822f;
    --orange-light: #f0a25a;
    --blue: #1f5aa6;
    --navy: #2b3a8c;
    --panel: #eceef7;
    --ink: #111111;
    --page: #ffffff;
    --backdrop: #f2f2f2;
  }
  html, body {
    margin: 0;
    width: 1200px;
    height: 1000px;
    overflow: hidden;
    background: var(--backdrop);
    font-family: "Arimo", Arial, sans-serif;
  }
  .flyer {
    position: absolute;
    left: 0;
    top: 35px;
    width: 1200px;
    height: 930px;
    background: var(--page);
  }
  .flyer svg { display: block; width: 100%; height: 100%; }
  .title { font: italic 700 24px "Arimo", Arial, sans-serif; fill: #fff; }
  .brand-name { font: 700 26px "Arimo", Arial, sans-serif; fill: var(--blue); }
  .brand-web { font: 700 8px "Arimo", Arial, sans-serif; fill: var(--blue); }
  .contact { font: 400 7.5px "Arimo", Arial, sans-serif; fill: var(--ink); }
  .step-box { fill: var(--orange); stroke: #fff; stroke-width: 1.5; }
  .step-ring { fill: none; stroke: var(--orange); stroke-width: 1.2; }
  .step-label { font: 700 11px "Arimo", Arial, sans-serif; fill: #fff; text-anchor: middle; }
  .cycle-label { font: 700 9px "Arimo", Arial, sans-serif; fill: #fff; text-anchor: middle; }
  .flow-arrow { stroke: var(--blue); stroke-width: 2; fill: none; }
  .cycle-arrow { stroke: var(--blue); stroke-width: 2; fill: none; }
  .panel-outer { fill: none; stroke: var(--navy); stroke-width: 1.2; }
  .panel-inner { fill: var(--panel); stroke: var(--navy); stroke-width: 1.2; }
  .panel-title { font: 700 11.5px "Arimo", Arial, sans-serif; fill: var(--navy); text-anchor: middle; }
  .connector-orange { stroke: var(--orange); stroke-width: 2.5; fill: none; }
  .connector-blue { stroke: var(--navy); stroke-width: 2.5; fill: none; }
  .task { font: 400 8.5px "Arimo", Arial, sans-serif; fill: var(--ink); }
</style>
</head>
<body>
<main class="flyer">
  <svg viewBox="0 0 800 620" xmlns="http://www.w3.org/2000/svg" role="img" aria-label="The BrightHarbor Process flowchart">
    <defs>
      <linearGradient id="title-band" x1="0" x2="1" y1="0" y2="0">
        <stop offset="0" stop-color="#e8822f" stop-opacity="0"/>
        <stop offset="0.45" stop-color="#e8822f" stop-opacity="0.85"/>
        <stop offset="1" stop-color="#e8822f"/>
      </linearGradient>
      <linearGradient id="task-orange" x1="0" x2="1" y1="0" y2="0">
        <stop offset="0" stop-color="#e8822f"/>
        <stop offset="0.35" stop-color="#f3b17a" stop-opacity="0.55"/>
        <stop offset="0.6" stop-color="#fff" stop-opacity="0"/>
      </linearGradient>
      <linearGradient id="task-blue" x1="0" x2="1" y1="0" y2="0">
        <stop offset="0" stop-color="#2b3a8c"/>
        <stop offset="0.2" stop-color="#8e96c8" stop-opacity="0.55"/>
        <stop offset="0.45" stop-color="#fff" stop-opacity="0"/>
      </linearGradient>
      <marker id="arrow-head" viewBox="0 0 10 10" refX="8" refY="5" markerWidth="5" markerHeight="5" orient="auto-start-reverse">
        <path d="M0 0 L10 5 L0 10 z" fill="#1f5aa6"/>
      </marker>
    </defs>

    <!-- Header -->
    <rect class="title-band" x="32" y="36" width="570" height="43" fill="url(#title-band)"/>
    <text class="title" x="567" y="66" text-anchor="end">The BrightHarbor Process</text>

    <circle class="brand-mark" cx="612" cy="58" r="13" fill="#1f5aa6"/>
    <text class="brand-name" x="632" y="68">NexaPoint</text>
    <text class="brand-web" x="780" y="90" text-anchor="end">www.nexapointit.com</text>
    <text class="brand-web" x="780" y="101" text-anchor="end">hello@nexapointit.com</text>
    <text class="contact" x="780" y="126" text-anchor="end">Phone: (555)014-2290</text>
    <text class="contact" x="780" y="138" text-anchor="end">4820 Cedar Ridge Rd., Suite 210</text>
    <text class="contact" x="780" y="150" text-anchor="end">Mesa AZ 85201</text>

    <!-- Step 1 -->
    <g class="step">
      <rect class="step-ring" x="34" y="266" width="106" height="53" rx="10"/>
      <rect class="step-box" x="36" y="268" width="102" height="49" rx="9"/>
      <text class="step-label" x="87" y="289">Assess</text>
      <text class="step-label" x="87" y="303">Alignment</text>
      <path class="connector-orange" d="M84 319 V340"/>
      <rect x="32" y="339" width="140" height="58" fill="url(#task-orange)"/>
      <text class="task" x="40" y="357">•&#160;&#160;Review Technology Philosophy</text>
      <text class="task" x="40" y="375">•&#160;&#160;Share Proprietary Method</text>
      <text class="task" x="40" y="393">•&#160;&#160;Assess Organizational Fit</text>
    </g>
    <path class="flow-arrow" d="M145 293 H184" marker-end="url(#arrow-head)"/>

    <!-- Step 2 -->
    <g class="step">
      <rect class="step-ring" x="192" y="266" width="106" height="53" rx="10"/>
      <rect class="step-box" x="194" y="268" width="102" height="49" rx="9"/>
      <text class="step-label" x="245" y="297">On Boarding</text>
      <path class="connector-orange" d="M242 319 V340"/>
      <rect x="193" y="339" width="140" height="76" fill="url(#task-orange)"/>
      <text class="task" x="201" y="357">•&#160;&#160;Establish Expectations</text>
      <text class="task" x="201" y="375">•&#160;&#160;Service Provider Transition</text>
      <text class="task" x="201" y="393">•&#160;&#160;Cybersecurity Review</text>
      <text class="task" x="201" y="411">•&#160;&#160;Backup/Protection Strategy</text>
    </g>
    <path class="flow-arrow" d="M302 293 H341" marker-end="url(#arrow-head)"/>

    <!-- Step 3 -->
    <g class="step">
      <rect class="step-ring" x="349" y="266" width="106" height="53" rx="10"/>
      <rect class="step-box" x="351" y="268" width="102" height="49" rx="9"/>
      <text class="step-label" x="402" y="289">30 Day</text>
      <text class="step-label" x="402" y="303">Evaluation</text>
      <path class="connector-orange" d="M400 319 V340"/>
      <rect x="350" y="339" width="140" height="76" fill="url(#task-orange)"/>
      <text class="task" x="358" y="357">•&#160;&#160;Develop IT Playbook</text>
      <text class="task" x="358" y="375">•&#160;&#160;Major Risk Identification</text>
      <text class="task" x="358" y="393">•&#160;&#160;Observe &amp; Document Trends</text>
      <text class="task" x="358" y="411">•&#160;&#160;Standards Alignment Plan</text>
    </g>
    <path class="flow-arrow" d="M459 293 H500" marker-end="url(#arrow-head)"/>

    <!-- Ongoing cycle panel -->
    <g class="cycle-panel">
      <rect class="panel-outer" x="506" y="191" width="253" height="206" rx="12"/>
      <rect class="panel-inner" x="509" y="194" width="247" height="200" rx="10"/>
      <text class="panel-title" x="632" y="215">Ongoing Strategic Plan &amp; Execution</text>

      <rect class="step-ring" x="596" y="229" width="77" height="38" rx="7"/>
      <rect class="step-box" x="597" y="230" width="75" height="36" rx="6"/>
      <text class="cycle-label" x="634" y="251">Strategy</text>

      <rect class="step-ring" x="517" y="284" width="77" height="39" rx="7"/>
      <rect class="step-box" x="518" y="285" width="75" height="37" rx="6"/>
      <text class="cycle-label" x="555" y="300">Risk</text>
      <text class="cycle-label" x="555" y="312">Assessment</text>

      <rect class="step-ring" x="674" y="284" width="77" height="39" rx="7"/>
      <rect class="step-box" x="675" y="285" width="75" height="37" rx="6"/>
      <text class="cycle-label" x="712" y="300">Standard</text>
      <text class="cycle-label" x="712" y="312">Alignment</text>

      <rect class="step-ring" x="596" y="337" width="77" height="39" rx="7"/>
      <rect class="step-box" x="597" y="338" width="75" height="37" rx="6"/>
      <text class="cycle-label" x="634" y="360">Budget</text>

      <path class="cycle-arrow" d="M553 275 Q545 250 588 247" marker-start="url(#arrow-head)" marker-end="url(#arrow-head)"/>
      <path class="cycle-arrow" d="M681 247 Q715 248 714 275" marker-start="url(#arrow-head)" marker-end="url(#arrow-head)"/>
      <path class="cycle-arrow" d="M714 332 Q715 358 681 358" marker-start="url(#arrow-head)" marker-end="url(#arrow-head)"/>
      <path class="cycle-arrow" d="M588 358 Q553 358 553 332" marker-start="url(#arrow-head)" marker-end="url(#arrow-head)"/>

      <path class="connector-blue" d="M575 397 V420"/>
      <rect x="524" y="419" width="200" height="93" fill="url(#task-blue)"/>
      <text class="task" x="532" y="435">•&#160;&#160;Develop &amp; Execute Annual Strategic Plan</text>
      <text class="task" x="532" y="453">•&#160;&#160;Risk Assessment, Ranking, Mitigation</text>
      <text class="task" x="532" y="471">•&#160;&#160;Prioritize Investments</text>
      <text class="task" x="532" y="489">•&#160;&#160;Develop 5 Year Budget</text>
      <text class="task" x="532" y="507">•&#160;&#160;NexaSolution™ Standard Alignment</text>
    </g>
  </svg>
</main>
</body>
</html>
```